Business Card Design for new logo

Business card Design for new logo. Follow colors from logo.
The company has offices in multiple comtries
Want to have some bulltes on the countries and also on the main services

Something like
USA*Dominican Republic*LATAM

Consulting*Healthcare IT*Tranformation

Industry/Entity Type

Information Technology

Contact Information for Business Card

Address, Phones, countries, name and position

Miron castell

Founder and CEO

947 Quarry Ln
Mill haven, PA 16835

Mcastell@novelquin.com

www.novelquin.com

717-352-6081

828-444-4444

```html
<!DOCTYPE html>
<html lang="en">
<head>
<meta charset="utf-8">
<title>Novelquin business card</title>
<link href="https://fonts.googleapis.com/css2?family=Lato:wght@400;700&display=swap" rel="stylesheet">
<style>
  :root {
    --brand-blue: #2f86c4;
    --brand-orange: #f0a15e;
    --card-dark: #2c2b30;
    --card-light: #f6f6f6;
    --ink: #2a2a2a;
    --muted-shape: #e3e3e3;
    --backdrop: #1e1e20;
  }
  * { margin: 0; padding: 0; box-sizing: border-box; }
  html, body { width: 1200px; height: 900px; overflow: hidden; }
  body {
    background: var(--backdrop);
    font-family: "Lato", sans-serif;
    position: relative;
  }
  .card {
    position: absolute;
    width: 520px;
    height: 297px;
    border-radius: 22px;
    overflow: hidden;
    box-shadow: 0 14px 30px rgba(0,0,0,0.5);
  }
  .card-back {
    left: 100px; top: 110px;
    background: var(--card-dark);
    display: flex; flex-direction: column;
    align-items: center; justify-content: center;
    text-align: center;
  }
  .brand {
    display: flex; align-items: center; gap: 12px;
    color: var(--brand-blue);
    font-weight: 700;
  }
  .brand-dot {
    border-radius: 50%;
    background: var(--brand-orange);
  }
  .card-back .brand { font-size: 50px; }
  .card-back .brand-dot { width: 30px; height: 30px; }
  .list-row {
    font-size: 15px;
    letter-spacing: 0.3px;
    margin-top: 12px;
  }
  .list-row span + span::before {
    content: "|";
    margin: 0 14px;
  }
  .countries { color: var(--brand-blue); margin-top: 18px; }
  .services { color: var(--brand-orange); margin-top: 22px; }

  .card-front {
    left: 580px; top: 490px;
    background: var(--card-light);
  }
  .decor-circle {
    position: absolute;
    right: -70px; top: 70px;
    width: 260px; height: 260px;
    border-radius: 50%;
    background: var(--muted-shape);
    opacity: 0.7;
  }
  .card-front .brand {
    position: absolute; right: 40px; top: 40px;
    font-size: 30px;
  }
  .card-front .brand-dot { width: 18px; height: 18px; }
  .person { position: absolute; left: 44px; top: 110px; }
  .person-name { color: var(--brand-blue); font-weight: 700; font-size: 22px; }
  .person-role { color: var(--brand-orange); font-size: 16px; margin-top: 2px; }
  .contacts {
    position: absolute; left: 44px; top: 182px;
    list-style: none;
    color: var(--ink);
    font-size: 15px;
    line-height: 22px;
  }
  .contacts li { display: flex; align-items: flex-start; gap: 10px; }
  .contacts svg { width: 14px; height: 14px; margin-top: 4px; flex: none; fill: var(--brand-orange); }
  .website {
    position: absolute; right: 40px; top: 188px;
    color: var(--brand-blue); font-size: 15px;
  }
</style>
</head>
<body>
  <section class="card card-back">
    <div class="brand"><span class="brand-dot"></span>Novelquin</div>
    <p class="list-row countries"><span>USA</span><span>Dominican Republic</span><span>LATAM</span></p>
    <p class="list-row services"><span>Consulting</span><span>Healthcare IT</span><span>Tranformation</span></p>
  </section>

  <section class="card card-front">
    <div class="decor-circle"></div>
    <div class="brand"><span class="brand-dot"></span>Novelquin</div>
    <div class="person">
      <p class="person-name">Miron castell</p>
      <p class="person-role">Founder and CEO</p>
    </div>
    <ul class="contacts">
      <li><svg viewBox="0 0 24 24"><path d="M3 9c0-3 4-5 9-5s9 2 9 5l-1 2-4-1V8c-3-1-5-1-8 0v2l-4 1zM6 13h12l2 7H4z"/></svg>717-352-6081</li>
      <li><svg viewBox="0 0 24 24"><path d="M3 9c0-3 4-5 9-5s9 2 9 5l-1 2-4-1V8c-3-1-5-1-8 0v2l-4 1zM6 13h12l2 7H4z"/></svg>828-444-4444</li>
      <li><svg viewBox="0 0 24 24"><path d="M2 5h20v14H2zM3 6l9 7 9-7v2l-9 7-9-7z" fill-rule="evenodd"/></svg>Mcastell@novelquin.com</li>
      <li><svg viewBox="0 0 24 24"><path d="M12 2a7 7 0 0 1 7 7c0 5-7 13-7 13S5 14 5 9a7 7 0 0 1 7-7zm0 4a3 3 0 1 0 0 6 3 3 0 0 0 0-6z" fill-rule="evenodd"/></svg><span>947 Quarry Ln<br>Mill haven, PA 16835</span></li>
    </ul>
    <p class="website">www.novelquin.com</p>
  </section>
</body>
</html>
```